Loomberry AI - Help users create their own recipe for a delicious AI treat!

Our company is an AI startup called Loomberrys. A Loomberry is an easy way to play with data (user can ask questions and get visualized answers about the dataset, sort of like QuillMate). Our users can "bake" their own Loomberrys by combining different sources of data.

We need a page that offers two things (both are required):

(1) TRY A LOOMBERRY --> Present a gallery of pre-made Loomberrys, each of which a user can click on and start playing with inside a popup iFrame. (visually, a Loomberry should be represented by some variation of our logo, attached). Designer does not need to worry about the iFrame popup.

(2) BAKE YOUR OWN LOOMBERRY --> Guide the user through making their own Loomberry recipe. The steps in making a Loomberry are:

A. Pick first ingredient - a Connector that imports the user's own data (visually, we present these options as logos for the Connector source, like Zentor, Pallomix, Brivane KLX, etc.).

B. Pick additional ingredients - the user can choose from 3rd-party cakes to combine with their own data added in (A). (visually, these 3rd-party cake options are presented as "mini" cakes, similar to our logo)

C. Once the ingredients are selected, the user can hit a BAKE button, and an iFrame popup opens, where user can play with the result. Designer does not need to worry about the iFrame popup.

We already have a web page and color scheme that we'd like this page to match (https://www.loomberrys.ai). The designer has freedom to play with format and try variations on the color scheme. The overall design should feel futuristic, fun, but also professional (like our logo).

Target Market(s)

Business users who want an easier way to get answers from large messy data

Industry/Entity Type

Tech/AI

Number of Pages Required

1 page

Font styles to use
Other font styles liked:
• Rubik

Requirements
Must have
• Full page design that matches current website (www.loomberrys.ai) and meets all requirements in the Project Description
Nice to have
• Included in the Project Description
Should not have
• Do not submit any designs that are too cartoonish or would not appeal to a business user

```html
<!DOCTYPE html>
<html lang="en">
<head>
<meta charset="utf-8">
<title>Loomberrys — Try or Bake a Loomberry</title>
<link href="https://fonts.googleapis.com/css2?family=Rubik:wght@300;400;500;700&display=swap" rel="stylesheet">
<style>
:root{
  --bg-top:#15203f;
  --bg-bottom:#0b1224;
  --panel:#131c36;
  --card:#1b2645;
  --card-dark:#0f1730;
  --line:#26365a;
  --cyan:#22d3ee;
  --pink:#e07ab5;
  --lime:#d7e36b;
  --white:#ffffff;
  --soft:#d5dbe8;
  --muted:#8f9ab3;
  --red:#ef5a6f;
  --grad:linear-gradient(90deg,#e07ab5,#22d3ee);
}
*{box-sizing:border-box;margin:0;padding:0}
html,body{width:883px;height:1200px;overflow:hidden}
body{
  position:relative;
  font-family:"Rubik",sans-serif;
  color:var(--white);
  background:linear-gradient(180deg,var(--bg-top) 0%,#111a35 40%,var(--bg-bottom) 100%);
}
.abs{position:absolute}
/* nav */
.brand{left:70px;top:18px;display:flex;align-items:center;gap:6px;font-size:20px;font-weight:300}
.brand-dot{width:14px;height:14px;border-radius:3px;background:var(--grad)}
.nav{left:468px;top:23px;display:flex;gap:15px;font-size:12px;color:var(--soft)}
.btn-grad{background:var(--grad);color:#10182e;font-weight:500;border-radius:20px;display:flex;align-items:center;justify-content:center}
.nav-cta{left:711px;top:14px;width:104px;height:32px;font-size:10.5px}
/* hero */
.hero-title{left:70px;top:197px;width:340px;font-size:22px;font-weight:700;line-height:28px}
.hero-sub{left:70px;top:266px;width:340px;font-size:14px;font-weight:500;line-height:18px;color:var(--cyan)}
.hero-copy{left:70px;top:322px;width:330px;font-size:9.8px;line-height:13.5px;color:var(--soft);font-weight:300}
.hero-copy p{margin-bottom:13px}
.hl-pink{color:var(--pink);font-weight:500}
.hl-lime{color:var(--lime);font-weight:500}
.hero-demo{left:70px;top:454px;width:104px;height:32px;font-size:10.5px}
.btn-line{border:1.5px solid var(--cyan);border-radius:20px;display:flex;align-items:center;justify-content:center;font-weight:500;color:var(--white)}
.hero-wait{left:189px;top:454px;width:117px;height:32px;font-size:10.5px}
/* try panel */
.try-head{left:560px;top:99px;width:172px;text-align:right}
.try-head h2{font-size:17px;font-weight:700;line-height:20px}
.try-head p{font-size:10.5px;color:var(--soft);font-weight:300}
.try-panel{left:474px;top:152px;width:362px;height:374px;border:1px solid var(--line);border-radius:10px;background:rgba(19,28,54,.55)}
.cake{position:absolute;width:149px;height:102px;border:1px solid var(--line);border-radius:4px;background:var(--card);font-size:7px;color:var(--soft)}
.cake .top{position:absolute;left:6px;right:6px;top:6px;display:flex;justify-content:space-between}
.cake .mark{position:absolute;left:58px;top:22px;width:32px;height:32px;border-radius:50%;border:1.5px solid #8f9ab3}
.cake .label{position:absolute;left:0;right:0;top:71px;border-top:1px solid var(--line);padding:11px 6px 0;font-size:7px;color:var(--white)}
.cake.selected{border-color:var(--cyan)}
.cake.selected .mark{border:none;background:var(--grad)}
.cake .note{position:absolute;left:0;right:0;top:108px;text-align:center;color:var(--cyan);font-size:7px}
.bake{border:1.5px solid var(--pink);border-radius:20px;display:flex;align-items:center;justify-content:center;font-size:11px;font-weight:700;letter-spacing:1.5px;border-right-color:var(--cyan);border-bottom-color:var(--cyan)}
/* bake section */
.bake-icon{left:336px;top:612px;width:30px;height:30px;border-radius:50%;background:var(--grad)}
.bake-head{left:379px;top:610px}
.bake-head h2{font-size:17px;font-weight:700}
.bake-head p{font-size:10.5px;color:var(--soft);font-weight:300}
.step{left:131px;width:622px;border:1px solid #1c2a4a;border-radius:4px;background:rgba(11,18,38,.6)}
.step-label{position:absolute;left:0;right:0;top:-10px;display:flex;justify-content:center}
.step-label span{display:flex;align-items:center;gap:6px;background:var(--bg-bottom);padding:0 6px;color:var(--cyan);font-size:11px;font-weight:500}
.num{width:16px;height:16px;border:1.3px solid var(--cyan);border-radius:50%;display:flex;align-items:center;justify-content:center;font-size:9px}
.step-desc{position:absolute;left:0;right:0;top:16px;text-align:center;font-size:7.8px;color:var(--soft)}
.provider{position:absolute;top:47px;width:172px;height:63px;border:1px solid var(--line);border-radius:3px;display:flex;align-items:center;justify-content:center;gap:10px}
.provider.on{border-color:var(--cyan)}
.provider .dot{width:26px;height:26px;border-radius:50%;background:#3b82f6}
.provider .dot.sq{border-radius:4px;background:#f5a524}
.provider .name{font-size:16px;line-height:16px}
.provider .name small{display:block;font-size:13px;color:var(--muted);font-weight:300}
.provider-note{position:absolute;top:123px;width:172px;text-align:center;font-size:7.8px;color:var(--cyan)}
.mini{position:absolute;top:47px;width:174px;height:96px;border:1px solid var(--line);border-radius:4px;background:var(--card-dark);font-size:7.8px;color:var(--muted)}
.mini.done{border-color:var(--cyan)}
.mini .top{position:absolute;left:6px;right:8px;top:6px;display:flex;justify-content:space-between}
.mini .mark{position:absolute;left:74px;top:20px;width:26px;height:26px;border-radius:50%;border:1.5px solid #8f9ab3}
.mini.done .mark{border:none;background:var(--grad)}
.mini .foot{position:absolute;left:0;right:0;top:58px;border-top:1px solid var(--line);padding:13px 8px 0 6px;display:flex;justify-content:space-between;letter-spacing:.5px}
.mini .foot .pct{color:var(--cyan)}
.mini.done .foot{color:var(--white)}
.mini.load .foot{color:var(--cyan)}
.mini.empty{border:1px dashed var(--line);background:none}
.add-btn{position:absolute;left:13px;top:55px;width:147px;height:25px;border:1px solid var(--pink);border-right-color:var(--cyan);border-radius:14px;display:flex;align-items:center;justify-content:center;gap:6px;font-size:8px;color:var(--white);letter-spacing:.5px}
.plus{width:12px;height:12px;border:1px solid var(--cyan);border-radius:50%;display:flex;align-items:center;justify-content:center;color:var(--cyan);font-size:10px;line-height:1}
.delete{position:absolute;top:146px;left:0;width:174px;text-align:center;color:var(--red);font-size:7.8px}
</style>
</head>
<body>
<header>
  <div class="abs brand"><span class="brand-dot"></span>loomberrys</div>
  <nav class="abs nav"><span>Try Pibbo</span><span>About Us</span><span>Contact Us</span></nav>
  <div class="abs btn-grad nav-cta">Try Web Demo</div>
</header>

<section class="hero">
  <h1 class="abs hero-title">Does your company have data that others would find useful?</h1>
  <p class="abs hero-sub">Our platform helps you monetize insights without exposing raw data</p>
  <div class="abs hero-copy">
    <p>You no longer need a large team of engineers to productize your data for external use.</p>
    <p>Introducing <span class="hl-pink">PIBBO</span>, our AI Data Concierge.</p>
    <p>Securely connect your cloud data, and let Pibbo guide users through <span class="hl-lime">Pick Your Own Path</span> insight generation, while keeping your <span class="hl-pink">raw data private</span>.</p>
  </div>
  <div class="abs btn-grad hero-demo">Try Web Demo</div>
  <div class="abs btn-line hero-wait">Join The Waitlist</div>
</section>

<section class="try">
  <div class="abs try-head"><h2>TRY A LOOMBERRY</h2><p>Select&nbsp; a Pre-made Loomberry</p></div>
  <div class="abs try-panel">
    <svg class="abs" style="left:167px;top:14px" width="28" height="16" viewBox="0 0 28 16"><path d="M1 15 L14 2 L27 15" fill="none" stroke="#4a5a80" stroke-width="1.3"/></svg>
    <div class="cake selected" style="left:22px;top:47px"><div class="top"><span>V3.10.23</span><span>5.3Gb</span></div><div class="mark"></div><div class="label">SMB Accounting</div><div class="note">Selected</div></div>
    <div class="cake" style="left:191px;top:47px"><div class="top"><span>V1.03.24</span><span>4.2Gb</span></div><div class="mark"></div><div class="label">TORI Loomberry</div></div>
    <div class="cake" style="left:22px;top:176px"><div class="top"><span>V1.03.24</span><span>4.2Gb</span></div><div class="mark"></div><div class="label">TORI Loomberry</div></div>
    <div class="cake" style="left:191px;top:176px"><div class="top"><span>V1.03.24</span><span>4.2Gb</span></div><div class="mark"></div><div class="label">TORI Loomberry</div></div>
    <svg class="abs" style="left:167px;top:295px" width="28" height="16" viewBox="0 0 28 16"><path d="M1 1 L14 14 L27 1" fill="none" stroke="#4a5a80" stroke-width="1.3"/></svg>
    <div class="abs bake" style="left:132px;top:331px;width:98px;height:31px">BAKE</div>
  </div>
</section>

<section class="build">
  <div class="abs bake-icon"></div>
  <div class="abs bake-head"><h2>Bake Your Own Loomberry</h2><p>Pick Your Own Ingredients</p></div>

  <div class="abs step" style="top:708px;height:140px">
    <div class="step-label"><span><span class="num">1</span>Pick Your First Ingredient</span></div>
    <div class="step-desc">Select One Of The Following Dataset Providers To Start Working On</div>
    <div class="provider" style="left:19px"><span class="dot"></span><span class="name">Pallomix<small>Dataset</small></span></div>
    <div class="provider" style="left:225px"><span class="dot sq"></span><span class="name">Brivane KLX<small>web services</small></span></div>
    <div class="provider on" style="left:431px"><span class="dot"></span><span class="name">Zentor<small>DeepTable</small></span></div>
    <div class="provider-note" style="left:431px">Configured</div>
  </div>

  <div class="abs step" style="top:890px;height:172px">
    <div class="step-label"><span><span class="num">2</span>Additional Ingredient</span></div>
    <div class="step-desc">Configure Your Own 3th Party Datasets, Once Configured You Can BAKE Your Loomberry</div>
    <div class="mini done" style="left:19px"><div class="top"><span>V1.03.24</span><span>1.5Gb</span></div><div class="mark"></div><div class="foot"><span>Cake LF87TTL</span><span class="pct">100% Done</span></div></div>
    <div class="delete" style="left:19px">Delete ⊗</div>
    <div class="mini load" style="left:225px"><div class="top"><span>V1.0</span><span>3.5Gb</span></div><div class="mark"></div><div class="foot"><span>Loading...</span><span>35%</span></div></div>
    <div class="mini empty" style="left:430px"><div class="mark" style="top:16px;border-color:#4a5a80"></div><div class="add-btn">Add 3th Party Dataset <span class="plus">+</span></div></div>
  </div>

  <div class="abs bake" style="left:393px;top:1103px;width:98px;height:31px">BAKE</div>
</section>
</body>
</html>
```